Academic and Business book cover

I need a book cover for my academic and business book.
The focus is in international / global negotiation and influence (how to negotiate across cultures).
The book will be published on Torvex, both in Vellor and printed edition. therefore I need something that works under Torvex guidelines.The final design should be elegant and still be able to stand out against the competition.
I would like to have orange+grey for the text colors on the cover, even if different options are welcome.
Title and my name are in the attached word doc.

Target Market(s)

graduates, Phds, from international business schools. Managers

Industry/Entity Type

Business

Font styles to use
Serif
Sans Serif

Colors

Designer to choose colors to be used in the design.

Requirements
Must have
• The title and my name should have elegant fonts.
Nice to have
• pictures of the world that don't have the "usual" Europe in the centre.

```html
<!DOCTYPE html>
<html lang="en">
<head>
<meta charset="utf-8">
<title>The 5Cs Blueprint — Cover Options</title>
<link rel="stylesheet" href="https://fonts.googleapis.com/css2?family=Marcellus&family=Marcellus+SC&display=swap">
<style>
  :root {
    --page: #ffffff;
    --teal: #1d6f78;
    --teal-band: #0f7582;
    --orange-map: #f5a623;
    --ink-dark: #3b3a2c;
    --maroon: #5a0f06;
    --navy-top: #0d4a8e;
    --navy-bottom: #062452;
    --gold: #f2b21a;
    --gold-band: #e3a417;
    --sky: #2a8fe6;
    --sky-light: #3aa0f0;
    --olive: #434538;
    --olive-map: #5e6449;
    --antique-gold: #d4b56a;
    --slate-map: #9fb3c3;
    --cover-w: 292px;
    --cover-h: 466px;
  }
  * { box-sizing: border-box; margin: 0; padding: 0; }
  html, body { width: 1200px; height: 1000px; overflow: hidden; background: var(--page); }
  .sheet { position: relative; width: 1200px; height: 1000px; }

  .cover {
    position: absolute; width: var(--cover-w); height: var(--cover-h); overflow: hidden;
    font-family: "Marcellus SC", "Marcellus", serif; text-align: center;
  }
  .cover--r1 { top: 15px; } .cover--r2 { top: 511px; }
  .cover--c1 { left: 121px; } .cover--c2 { left: 458px; } .cover--c3 { left: 803px; }

  .cover__title { position: absolute; top: 44px; left: 0; right: 0; color: var(--title); line-height: 1; font-weight: 400; }
  .cover__title-main { display: block; font-size: 56px; letter-spacing: 1px; }
  .cover__title-sub { display: block; font-size: 34px; margin-top: 4px; letter-spacing: 0.5px; }
  .cover__rule { position: absolute; top: 148px; left: 17px; right: 13px; height: 1px; background: var(--rule); }
  .cover__subtitle { position: absolute; top: 158px; left: 30px; right: 26px; font-size: 13.5px; line-height: 17px; color: var(--sub); }
  .cover__rule--short { top: 225px; left: 54px; right: 46px; }

  .cover__map {
    position: absolute; top: 240px; left: 6px; right: 6px; height: 152px;
    border-radius: 40% 45% 35% 40%;
    background: radial-gradient(ellipse at 50% 45%, var(--map) 0%, var(--map) 45%, transparent 75%);
  }

  .cover__band {
    position: absolute; top: 396px; left: 0; right: 0; height: 56px; background: var(--band);
    display: flex; align-items: center; justify-content: center;
    font-size: 24px; color: var(--name);
  }
  .cover__band::before, .cover__band::after {
    content: ""; position: absolute; left: 0; right: 0; height: 1px; background: var(--band-line);
  }
  .cover__band::before { top: 4px; } .cover__band::after { bottom: 4px; }
  .cover__band--case { font-family: "Marcellus", serif; }

  .cover--silver { background: linear-gradient(160deg, #d0d0d0 0%, #e6e6e6 35%, #c4c4c4 70%, #b8b8b8 100%);
    --title: var(--teal); --sub: var(--teal); --rule: var(--teal); --map: var(--orange-map);
    --band: var(--teal-band); --name: #f1f4f4; --band-line: rgba(255,255,255,0.35); }
  .cover--amber { background: radial-gradient(ellipse at 50% 35%, #fbe07a 0%, #f7c247 40%, #f0951e 100%);
    --title: var(--ink-dark); --sub: #4a3f20; --rule: #6a5a2a; --map: rgba(120,110,50,0.55);
    --band: var(--maroon); --name: #f4e9df; --band-line: rgba(240,150,60,0.5); }
  .cover--navy { background: radial-gradient(ellipse at 50% 55%, #1d6fc0 0%, var(--navy-top) 45%, var(--navy-bottom) 100%);
    --title: var(--gold); --sub: var(--gold); --rule: var(--gold); --map: rgba(50,150,210,0.7);
    --band: var(--gold-band); --name: #24324f; --band-line: rgba(255,240,190,0.6); }
  .cover--sky { background: #a9a9a6;
    --title: #ffffff; --sub: #ffffff; --rule: #e8f3fd; --map: #c6c6c3;
    --band: var(--sky); --name: #ffffff; --band-line: rgba(255,255,255,0.5); }
  .cover--sky .cover__panel { position: absolute; top: 30px; left: 0; right: 0; height: 202px;
    background: linear-gradient(180deg, var(--sky) 0%, var(--sky-light) 100%); }
  .cover--olive { background: var(--olive);
    --title: var(--antique-gold); --sub: var(--antique-gold); --rule: var(--antique-gold); --map: var(--olive-map);
    --band: linear-gradient(90deg, #b8923f 0%, #f0d68a 50%, #b8923f 100%); --name: #2b2a22; --band-line: rgba(90,70,30,0.5); }
  .cover--olive .cover__title { background: linear-gradient(180deg, #f3dd9a 0%, #b88e3c 100%);
    -webkit-background-clip: text; background-clip: text; color: transparent; }
  .cover--pearl { background: radial-gradient(ellipse at 50% 50%, #f2f2f2 0%, #d6d6d6 60%, #c2c2c2 100%);
    --title: var(--teal); --sub: var(--teal); --rule: var(--teal); --map: var(--slate-map);
    --band: var(--teal-band); --name: #f1f4f4; --band-line: rgba(255,255,255,0.35); }
</style>
</head>
<body>
<main class="sheet">

  <section class="cover cover--silver cover--r1 cover--c1">
    <h1 class="cover__title"><span class="cover__title-main">THE 5CS</span><span class="cover__title-sub">BLUEPRINT</span></h1>
    <div class="cover__rule"></div>
    <p class="cover__subtitle">Practical Bargaining and Persuasion Methods for Cross-Border Success</p>
    <div class="cover__rule cover__rule--short"></div>
    <div class="cover__map" role="img" aria-label="Orange world map centred on Asia and the Pacific"></div>
    <div class="cover__band">DARIUS M. KOVEL</div>
  </section>

  <section class="cover cover--amber cover--r1 cover--c2">
    <h1 class="cover__title"><span class="cover__title-main">THE 5CS</span><span class="cover__title-sub">BLUEPRINT</span></h1>
    <div class="cover__rule"></div>
    <p class="cover__subtitle">Practical Bargaining and Persuasion Methods for Cross-Border Success</p>
    <div class="cover__rule cover__rule--short"></div>
    <div class="cover__map" role="img" aria-label="Olive world map centred on Asia and the Pacific"></div>
    <div class="cover__band cover__band--case">Darius M. Kovel</div>
  </section>

  <section class="cover cover--navy cover--r1 cover--c3">
    <h1 class="cover__title"><span class="cover__title-main">THE 5CS</span><span class="cover__title-sub">BLUEPRINT</span></h1>
    <div class="cover__rule"></div>
    <p class="cover__subtitle">Practical Bargaining and Persuasion Methods for Cross-Border Success</p>
    <div class="cover__rule cover__rule--short"></div>
    <div class="cover__map" role="img" aria-label="Glowing blue world map centred on Asia and the Pacific"></div>
    <div class="cover__band cover__band--case">Darius M. Kovel</div>
  </section>

  <section class="cover cover--sky cover--r2 cover--c1">
    <div class="cover__panel"></div>
    <h1 class="cover__title"><span class="cover__title-main">THE 5CS</span><span class="cover__title-sub">BLUEPRINT</span></h1>
    <div class="cover__rule"></div>
    <p class="cover__subtitle">Practical Bargaining and Persuasion Methods for Cross-Border Success</p>
    <div class="cover__rule cover__rule--short"></div>
    <div class="cover__map" role="img" aria-label="Light grey world map centred on Asia and the Pacific"></div>
    <div class="cover__band">DARIUS M. KOVEL</div>
  </section>

  <section class="cover cover--olive cover--r2 cover--c2">
    <h1 class="cover__title"><span class="cover__title-main">THE 5CS</span><span class="cover__title-sub">BLUEPRINT</span></h1>
    <div class="cover__rule"></div>
    <p class="cover__subtitle">Practical Bargaining and Persuasion Methods for Cross-Border Success</p>
    <div class="cover__rule cover__rule--short"></div>
    <div class="cover__map" role="img" aria-label="Muted olive world map centred on Asia and the Pacific"></div>
    <div class="cover__band cover__band--case">Darius M. Kovel</div>
  </section>

  <section class="cover cover--pearl cover--r2 cover--c3">
    <h1 class="cover__title"><span class="cover__title-main">THE 5CS</span><span class="cover__title-sub">BLUEPRINT</span></h1>
    <div class="cover__rule"></div>
    <p class="cover__subtitle">Practical Bargaining and Persuasion Methods for Cross-Border Success</p>
    <div class="cover__rule cover__rule--short"></div>
    <div class="cover__map" role="img" aria-label="Slate blue world map centred on Asia and the Pacific"></div>
    <div class="cover__band">DARIUS M. KOVEL</div>
  </section>

</main>
</body>
</html>
```